VELMIT Business Card

VELMIT (www.velmitpools.example) is a veteran in the swimming pool maintenance and repair business..we have served our clients for 15 years and have a research chemist, an electrician, a plumber and a pool building contractor (in part) on staff...We want to provide a business card that has a dual purpose, that people want to keep around, that leaves people speechless in the sense that they understand the mission of and the experience level of the TEAM at VELMIT.

Target Market(s)

persons who enjoy swimming and make it a priority to swim

Industry/Entity Type

Building

Font styles to use
Serif
Sans Serif

Colors
85acd3
3176b5
95b6d8
3276b5
0355a3
0555a3
0255a3
0455a3
85abd2

Requirements
Must have
• name, title, address, email, text
Nice to have
• a die cut shape
Should not have
• cartoons, pictures of pools

```html
<!DOCTYPE html>
<html lang="en">
<head>
<meta charset="utf-8">
<title>VELMIT Business Card</title>
<link href="https://fonts.googleapis.com/css2?family=Roboto+Condensed:wght@700&display=swap" rel="stylesheet">
<style>
  :root {
    --canvas-bg: #e4e6e8;
    --card-white: #ffffff;
    --card-white-shade: #eef1f5;
    --water-deep: #1f7fc4;
    --water-mid: #3aa0dc;
    --water-light: #85c8ee;
    --wave-light: #95b6d8;
    --wave-pale: #c3d8ee;
    --wave-strong: #3276b5;
    --brand-teal: #3aa6c8;
    --url-cyan: #4fd3ec;
    --text-white: #ffffff;
  }
  * { margin: 0; padding: 0; box-sizing: border-box; }
  html, body { width: 1200px; height: 1000px; overflow: hidden; }
  body {
    background: var(--canvas-bg);
    font-family: "Roboto Condensed", "Arial Narrow", sans-serif;
    font-weight: 700;
    position: relative;
  }
  .card {
    position: absolute;
    width: 525px;
    height: 300px;
    border-radius: 26px;
    overflow: hidden;
    box-shadow: 0 6px 18px rgba(0,0,0,0.18);
  }
  /* Back side */
  .card-back {
    left: 100px;
    top: 170px;
  }
  .water-fill {
    position: absolute;
    inset: 0;
    background:
      radial-gradient(ellipse at 70% 20%, var(--water-light) 0%, transparent 55%),
      linear-gradient(160deg, var(--water-mid) 0%, var(--water-deep) 100%);
  }
  .back-text {
    position: absolute;
    color: var(--text-white);
    text-shadow: 0 1px 2px rgba(0,0,0,0.35);
    white-space: nowrap;
  }
  .tollfree { left: 34px; top: 40px; font-size: 15px; letter-spacing: 0.3px; }
  .contact-block { left: 262px; top: 84px; text-align: left; }
  .person-name { font-size: 19px; }
  .person-title { font-size: 12px; margin-left: 10px; margin-bottom: 16px; }
  .person-phone { font-size: 20px; margin-bottom: 18px; }
  .person-email { font-size: 17px; }
  .address { right: 24px; bottom: 40px; font-size: 12px; }

  /* Front side */
  .card-front {
    left: 575px;
    top: 480px;
    background: linear-gradient(180deg, var(--card-white) 0%, var(--card-white-shade) 100%);
  }
  .waves { position: absolute; inset: 0; }
  .brand {
    position: absolute;
    left: 120px;
    top: 70px;
    display: flex;
    flex-direction: column;
    align-items: flex-start;
  }
  .brand-name {
    display: flex;
    align-items: center;
    gap: 10px;
    color: var(--brand-teal);
    font-size: 62px;
    line-height: 1;
    letter-spacing: 1px;
  }
  .brand-mark {
    width: 18px;
    height: 18px;
    background: var(--brand-teal);
  }
  .brand-url {
    margin-top: 6px;
    color: var(--url-cyan);
    font-size: 18px;
    letter-spacing: 0.5px;
    text-transform: uppercase;
  }
</style>
</head>
<body>

<section class="card card-back">
  <div class="water-fill" role="img" aria-label="Rippling clear blue pool water photograph"></div>
  <p class="back-text tollfree">CALL US TOLL-FREE: 1-877-555-SWIM</p>
  <div class="back-text contact-block">
    <p class="person-name">Dana Rivers</p>
    <p class="person-title">Director</p>
    <p class="person-phone">760-555-0142</p>
    <p class="person-email">dana@velmitpools.example</p>
  </div>
  <p class="back-text address">1820 Harbor Lane Coral Vista, CA 90000</p>
</section>

<section class="card card-front">
  <svg class="waves" viewBox="0 0 525 300" preserveAspectRatio="none" aria-hidden="true">
    <path d="M0 236 C120 222 200 210 270 160 C340 105 420 70 525 64 L525 80 C430 92 360 120 300 170 C230 228 120 250 0 262 Z" fill="var(--wave-light)"/>
    <path d="M0 262 C120 250 230 228 300 170 C360 120 430 92 525 80 L525 300 L0 300 Z" fill="var(--wave-pale)" opacity="0.55"/>
    <path d="M0 228 C110 220 190 205 255 170" fill="none" stroke="var(--wave-strong)" stroke-width="5"/>
    <path d="M330 128 C390 95 450 80 525 72" fill="none" stroke="var(--wave-strong)" stroke-width="5"/>
  </svg>
  <div class="brand">
    <div class="brand-name"><span class="brand-mark"></span>VELMIT</div>
    <p class="brand-url">www.velmitpools.example</p>
  </div>
</section>

</body>
</html>
```